Local Computer Repair Business needs Flyer Design

I am looking for a small postcard sized (4x6) advertisement but use the full space 4x6. We are a local computer repair shop that provide sales and service of computer systems, any models, any problems. We also offer E-cycling for our customers. This will be distributed via post office box.
Emphasize shop locally, best service around, professional, Competitive prices.
One side for computer sales/repair and the other side should be E-Cycling. we'll receive old laptops, desktop computers, tablets, game consoles, etc..
Ad must include the attached logo.
Ad must include address - 872 Larkspur Ave. Hudson, IA 50619
Ad must include phone number and website - 319-555-0174 and www.quillbyrnservices.com

```html
<!DOCTYPE html>
<html lang="en">
<head>
<meta charset="utf-8">
<title>Quillbyrn Services – Postcard Front and Back</title>
<link rel="stylesheet" href="https://fonts.googleapis.com/css2?family=Roboto+Condensed:ital,wght@0,300;0,400;0,700;1,400;1,800;1,900&family=Roboto:wght@400&display=swap">
<style>
  :root {
    --backdrop: #b3b3b3;
    --card-bg-light: #eef5f8;
    --red: #e0202a;
    --blue: #124f93;
    --green: #3a9a43;
    --white: #ffffff;
    --ink: #1d2b3a;
  }
  * { box-sizing: border-box; margin: 0; padding: 0; }
  html, body { width: 1200px; height: 1200px; overflow: hidden; }
  body {
    background: var(--backdrop);
    font-family: "Roboto Condensed", Arial, sans-serif;
    position: relative;
  }
  .postcard {
    position: absolute;
    left: 198px;
    width: 802px;
    height: 535px;
    overflow: hidden;
  }
  .postcard--repair { top: 55px; background: linear-gradient(90deg, #e4e8ea 0%, #dfe4e7 50%, #eef0f1 100%); }
  .postcard--ecycle { top: 620px; background: var(--card-bg-light); }

  .photo { position: absolute; }
  .postcard--repair .photo {
    left: 380px; top: 0; width: 422px; height: 535px;
    background:
      radial-gradient(ellipse 40% 70% at 92% 55%, #1e252e 0%, #2a313a 60%, rgba(42,49,58,0) 100%),
      radial-gradient(ellipse 35% 45% at 45% 75%, #39424c 0%, rgba(57,66,76,0) 100%),
      linear-gradient(90deg, rgba(228,232,234,1) 0%, rgba(228,232,234,0) 18%),
      linear-gradient(180deg, #f3f4f5 0%, #e1e5e8 30%, #9aa3ab 62%, #4c5560 100%);
  }
  .postcard--ecycle .photo {
    left: 354px; top: 192px; width: 448px; height: 343px;
    background:
      radial-gradient(ellipse 38% 42% at 74% 74%, #3fa246 0%, #4aa851 45%, rgba(74,168,81,0) 100%),
      radial-gradient(ellipse 30% 25% at 40% 40%, #f2f4f5 0%, rgba(242,244,245,0) 100%),
      linear-gradient(160deg, #c9ced2 0%, #8d959c 45%, #5d656d 80%, #7a838a 100%);
    clip-path: polygon(32% 14%, 100% 0, 100% 100%, 26% 100%, 0 72%, 12% 48%);
  }

  .headline {
    position: absolute;
    font-style: italic;
    font-weight: 900;
    color: var(--red);
    text-align: center;
    letter-spacing: -1px;
  }
  .postcard--repair .headline { left: 30px; top: 22px; width: 330px; font-size: 57px; line-height: 0.88; }
  .postcard--ecycle .headline { left: 18px; top: 24px; width: 380px; font-size: 54px; line-height: 0.93; }

  .band {
    position: absolute;
    left: 0; top: 242px;
    width: 376px; height: 101px;
    clip-path: polygon(0 0, 100% 0, 95% 100%, 0 100%);
    color: var(--white);
    text-align: center;
    padding-right: 18px;
  }
  .band--blue { background: var(--blue); }
  .band--green { background: var(--green); }
  .band__title { font-weight: 700; font-size: 42px; line-height: 1; padding-top: 9px; letter-spacing: -0.5px; }
  .band__sub { font-weight: 300; font-size: 30px; line-height: 1.1; margin-top: 3px; letter-spacing: -0.3px; }

  .brand {
    position: absolute;
    left: 25px; top: 370px; width: 345px;
    display: flex; align-items: center; justify-content: center; gap: 10px;
    white-space: nowrap;
  }
  .brand__dot { width: 30px; height: 30px; border-radius: 50%; background: var(--blue); flex: none; }
  .brand__name { font-weight: 700; font-size: 25px; color: var(--blue); letter-spacing: 0.3px; }

  .contact { position: absolute; left: 0; width: 385px; text-align: center; white-space: nowrap; }
  .contact__phone { top: 427px; font-weight: 700; font-size: 33px; line-height: 38px; color: var(--blue); }
  .contact__web { top: 467px; font-family: "Roboto", Arial, sans-serif; font-size: 18px; line-height: 22px; color: var(--red); letter-spacing: 0.6px; }
  .contact__address { top: 494px; font-size: 15px; line-height: 18px; color: var(--ink); }

  .taglines {
    position: absolute;
    left: 418px; top: 42px; width: 300px;
    transform: rotate(-7deg);
    font-style: italic; font-weight: 800;
    font-size: 33px; line-height: 1.4;
    text-align: center;
    white-space: nowrap;
  }
  .taglines .is-red { color: var(--red); }
  .taglines .is-blue { color: var(--blue); }

  .offer {
    position: absolute;
    left: 428px; top: 34px; width: 300px;
    transform: rotate(-7deg);
    text-align: center;
    color: var(--blue);
    font-style: italic; font-weight: 900;
    font-size: 44px; line-height: 1.05;
    white-space: nowrap;
  }
  .offer__note { display: block; font-weight: 400; font-style: italic; font-size: 13px; color: var(--ink); margin-top: 4px; }
</style>
</head>
<body>

<section class="postcard postcard--repair" aria-label="Postcard front: sales and repair">
  <div class="photo" role="img" aria-label="Photo of a technician holding an open laptop in a server room"></div>
  <h1 class="headline">Solutions<br>to all your<br>Technology<br>Needs.</h1>
  <p class="taglines">
    <span class="is-red">Best service around</span><br>
    <span class="is-blue">Competitive prices</span><br>
    <span class="is-red">Local ownership</span>
  </p>
  <div class="band band--blue">
    <p class="band__title">Sales &amp; Repair</p>
    <p class="band__sub">Any models, any problems.</p>
  </div>
  <div class="brand"><span class="brand__dot"></span><span class="brand__name">QUILLBYRN SERVICES, LLC</span></div>
  <p class="contact contact__phone">319-555-0174</p>
  <p class="contact contact__web">www.quillbyrnservices.com</p>
  <p class="contact contact__address">872 Larkspur Ave. Hudson, IA 50619</p>
</section>

<section class="postcard postcard--ecycle" aria-label="Postcard back: e-cycling">
  <div class="photo" role="img" aria-label="Photo of a pile of old laptops with a green recycling symbol"></div>
  <h2 class="headline">Time to replace<br>your old<br>or broken<br>electronics?</h2>
  <p class="offer">Optional<br>Data Destruction<br>service available.<span class="offer__note">*Additional fees apply</span></p>
  <div class="band band--green">
    <p class="band__title">Give us a call!</p>
    <p class="band__sub">E-cycling with safe disposal</p>
  </div>
  <div class="brand"><span class="brand__dot"></span><span class="brand__name">QUILLBYRN SERVICES, LLC</span></div>
  <p class="contact contact__phone">319-555-0174</p>
  <p class="contact contact__web">www.quillbyrnservices.com</p>
  <p class="contact contact__address">872 Larkspur Ave. Hudson, IA 50619</p>
</section>

</body>
</html>
```